Manufacturer's Representative Group needs a clean new Website

We represent and sell a number of suppliers that design and build products used in Biopharmaceutical manufacturing. Our sales region is in the central US. Our customer base is scientific / engineering based - so clean, we organized design with a focus on the products - easy and clear navigation is necessary. We do not sell direct or warehouse product - so e-commerce is not needed. Our customers will use the website for reference on what we do and offer - we will use the site as a platform to present products from each vendor and the home page will be used to capture an overview and draw users deeper into the site. You can view our current site - which needs A LOT of help to get ideas on products represented and types of products

Target Market(s)

Engineers and Pharmaceutical / Bio pharm end users

Industry/Entity Type

E-Commerce

Number of Pages Required

2 page

Font styles to use
Sans Serif

Requirements
Must have
• I need a home page that provides a snapshot of my company and the product lines we represent - then a second page that I can copy as a template for each line I rep as well as for an "About us / contact" page.
• I would like to be able to manage content on the pages so something easy to adjust pictures or add content is a must
• Must use our logo

```html
<!DOCTYPE html>
<html lang="en">
<head>
<meta charset="utf-8">
<title>Prairie Bio</title>
<link rel="stylesheet" href="https://fonts.googleapis.com/css2?family=Lato:ital,wght@0,300;0,400;0,700;0,900;1,400&display=swap">
<style>
:root{
  --orange:#f05a22;
  --orange-dark:#d94c17;
  --navy:#2b2960;
  --ink:#222;
  --grey-text:#666;
  --light:#f3f3f3;
  --line:#ddd;
  --footer:#262626;
  --white:#fff;
}
*{box-sizing:border-box;margin:0;padding:0}
html,body{width:1200px;height:2909px;overflow:hidden}
body{font-family:'Lato',sans-serif;color:var(--ink);background:var(--white);position:relative}
.abs{position:absolute}

/* top bar */
.topbar{position:absolute;left:0;top:0;width:1200px;height:48px;background:#f7f7f7;border-bottom:1px solid #e6e6e6}
.topbar .call{left:53px;top:14px;font-size:14px;font-weight:700;color:var(--navy);letter-spacing:1px}
.topbar .phone{left:128px;top:8px;display:flex;align-items:center;gap:10px;font-size:22px;font-weight:700;color:var(--navy)}
.search{left:812px;top:9px;width:344px;height:30px;border:1px solid #bbb;background:var(--white)}
.search svg{position:absolute;right:8px;top:6px}

/* header */
.header{position:absolute;left:0;top:48px;width:1200px;height:105px;background:var(--white)}
.brand{left:53px;top:30px;display:flex;align-items:center;gap:12px;font-size:40px;font-weight:700;color:var(--navy)}
.brand .dot{width:34px;height:34px;border-radius:50%;background:var(--orange)}
.nav{left:0;top:0;height:105px;width:1200px}
.nav a{position:absolute;top:0;height:105px;line-height:105px;font-size:13px;font-style:italic;color:var(--navy);text-decoration:none;letter-spacing:.5px}
.nav a.active{background:var(--navy);color:var(--white);width:94px;text-align:center}

/* hero */
.hero{position:absolute;left:0;top:153px;width:1200px;height:804px;background:linear-gradient(160deg,#4a5a72 0%,#8d3a2a 35%,#c7c7c7 60%,#6d7a8a 100%)}
.hero-title{left:0;top:90px;width:1200px;text-align:center;font-size:60px;font-weight:300;color:var(--white);line-height:80px;letter-spacing:1px}
.hero-dots{left:360px;top:240px;width:480px;border-top:3px dotted rgba(255,255,255,.85)}
.hero-text{left:150px;top:290px;width:900px;text-align:center;font-size:19px;line-height:30px;color:var(--white)}
.btn-hero{left:415px;top:436px;width:387px;height:58px;background:var(--orange);color:var(--white);font-size:17px;text-align:center;line-height:58px;letter-spacing:.5px}

/* feature cards */
.card{position:absolute;top:708px;width:252px;height:485px;background:var(--white)}
.card .head{position:absolute;left:0;top:0;width:252px;height:244px;background:var(--orange)}
.card .icon{position:absolute;left:90px;top:36px;width:72px;height:72px;border-radius:50%;background:var(--white);display:flex;align-items:center;justify-content:center}
.card .title{position:absolute;left:0;width:252px;text-align:center;font-size:24px;color:var(--white);letter-spacing:.5px}
.card .body{position:absolute;left:0;top:244px;width:252px;height:241px;padding:18px 18px 0;text-align:center;font-size:13px;line-height:19px;color:var(--grey-text)}
.card .plus{position:absolute;right:0;bottom:0;width:44px;height:44px;background:var(--orange);color:var(--white);font-size:26px;text-align:center;line-height:42px}
.card.lab .head{height:155px}
.card.lab .label{position:absolute;left:0;top:155px;width:252px;height:90px;background:var(--white);color:var(--orange);text-align:center;line-height:90px;font-size:24px}
.card.lab .body{background:var(--orange);color:var(--white)}
.card.lab .plus{background:var(--orange-dark)}
.shadow{left:0;top:1215px;width:1200px;height:40px;background:radial-gradient(ellipse 70% 100% at 50% 0,rgba(0,0,0,.45),rgba(0,0,0,0) 70%)}

/* products */
.section-title{left:0;top:1318px;width:1200px;text-align:center;font-size:34px;color:var(--orange);letter-spacing:1px}
.product{position:absolute;top:1391px;width:258px;height:281px;border:1px solid var(--line)}
.product .photo{height:200px;background:linear-gradient(180deg,#fafafa,#e4e4e4)}
.product .bar{position:absolute;left:0;bottom:0;width:100%;height:80px;background:var(--navy);color:var(--white);font-size:16px;line-height:80px;padding-left:16px;letter-spacing:.5px}
.product .bar span{position:absolute;right:0;top:0;width:46px;height:80px;background:var(--orange);text-align:center;font-size:22px}
.arrow-round{position:absolute;width:46px;height:46px;border-radius:50%;background:var(--orange);color:var(--white);text-align:center;line-height:44px;font-size:24px}

/* welcome + blog */
.about{left:0;top:1745px;width:1200px;height:412px;background:var(--light)}
.welcome-kicker{left:56px;top:33px;font-size:32px;font-weight:300;color:var(--navy)}
.welcome-name{left:56px;top:68px;font-size:54px;font-weight:300;color:var(--orange)}
.welcome-text{left:56px;top:128px;width:528px;font-size:14.5px;line-height:21px;color:var(--ink)}
.btn-navy{position:absolute;height:44px;background:var(--navy);color:var(--white);font-size:15px;line-height:44px;padding-left:22px}
.btn-navy span{position:absolute;right:0;top:0;width:24px;height:44px;background:var(--orange);text-align:center}
.divider{left:650px;top:30px;width:2px;height:350px;background:var(--orange)}
.blog-title{left:696px;top:22px;font-size:26px;color:var(--orange)}
.blog-photo{left:776px;top:61px;width:278px;height:145px;background:linear-gradient(135deg,#e9ecef,#c9cdd2 60%,#d9b69a)}
.blog-post-title{left:660px;top:217px;width:540px;text-align:center;font-size:14px;font-weight:700;color:var(--orange)}
.blog-text{left:690px;top:240px;width:460px;text-align:center;font-size:14px;line-height:20px;color:var(--grey-text)}
.blog-meta{left:820px;top:288px;display:flex;gap:40px;font-size:13px;color:var(--grey-text);align-items:center}
.blog-meta div{display:flex;gap:8px;align-items:center}

/* testimonial */
.testimonial{left:0;top:2157px;width:1200px;height:320px;background:linear-gradient(90deg,#6a7f8e 0%,#8a8a9a 30%,#4d7a5a 55%,#7e5fa0 80%,#9a7fb8 100%)}
.testimonial .shade{position:absolute;inset:0;background:rgba(40,40,50,.35)}
.t-arrow{position:absolute;top:135px;color:var(--white);font-size:48px;font-weight:300}
.quote-circle{left:182px;top:86px;width:146px;height:146px;border-radius:50%;background:var(--white);color:var(--orange);font-size:60px;font-weight:900;line-height:150px;padding-left:36px}
.avatar-circle{left:255px;top:86px;width:146px;height:146px;border-radius:50%;background:var(--orange);display:flex;align-items:center;justify-content:center}
.t-line{left:400px;top:80px;width:2px;height:160px;background:rgba(255,255,255,.6)}
.t-title{left:431px;top:76px;font-size:18px;font-weight:700;color:var(--orange);letter-spacing:.5px}
.t-text{left:431px;top:108px;width:660px;font-size:15.5px;line-height:22px;color:var(--white)}
.t-name{left:431px;top:256px;font-size:14px;font-weight:700;color:var(--white)}
.t-role{left:431px;top:276px;font-size:11px;font-weight:700;color:var(--white)}

/* newsletter */
.news{left:0;top:2477px;width:1200px;height:197px;background:var(--light)}
.news-title{left:0;top:63px;width:1200px;text-align:center;font-size:18px;color:var(--grey-text);letter-spacing:1px}
.news-input{left:322px;top:107px;width:437px;height:40px;background:var(--white);font-size:12px;color:#999;line-height:40px;padding-left:14px}
.news-submit{left:763px;top:107px;width:163px;height:40px;background:var(--orange);color:var(--white);font-weight:700;font-size:14px;text-align:center;line-height:40px}

/* footer */
.footer{left:0;top:2674px;width:1200px;height:235px;background:var(--footer);color:var(--white)}
.social{position:absolute;top:46px;width:42px;height:42px;border-radius:50%;background:var(--white)}
.f-address{left:286px;top:136px;display:flex;align-items:center;gap:18px;font-size:15px}
.f-phone{left:700px;top:130px;display:flex;align-items:center;gap:16px;font-size:26px;font-weight:700}
.f-copy{left:0;top:194px;width:1200px;text-align:center;font-size:12px}
</style>
</head>
<body>

<div class="topbar">
  <div class="abs call">CALL US</div>
  <div class="abs phone">
    <svg width="22" height="22" viewBox="0 0 24 24"><path fill="#2b2960" d="M6.6 10.8a15 15 0 0 0 6.6 6.6l2.2-2.2a1 1 0 0 1 1-.25 11.4 11.4 0 0 0 3.6.57 1 1 0 0 1 1 1V20a1 1 0 0 1-1 1A17 17 0 0 1 3 4a1 1 0 0 1 1-1h3.5a1 1 0 0 1 1 1c0 1.25.2 2.45.57 3.57a1 1 0 0 1-.25 1z"/></svg>
    1-800-555-0142
  </div>
  <div class="abs search">
    <svg width="16" height="16" viewBox="0 0 16 16"><circle cx="6.5" cy="6.5" r="5" fill="none" stroke="#2b2960" stroke-width="2"/><line x1="10" y1="10" x2="15" y2="15" stroke="#2b2960" stroke-width="2"/></svg>
  </div>
</div>

<header class="header">
  <div class="abs brand"><span class="dot"></span>Prairie Bio</div>
  <nav class="abs nav">
    <a class="active" style="left:478px">HOME</a>
    <a style="left:608px">ABOUT US</a>
    <a style="left:712px">PRODUCTS</a>
    <a style="left:848px">RESEARCH</a>
    <a style="left:978px">BLOG</a>
    <a style="left:1076px">CONTACT US</a>
  </nav>
</header>

<section class="hero" role="img" aria-label="Laboratory photo with microscope and orange petri dish">
  <h1 class="abs hero-title">OFFERING THE HIGHEST<br>QUALITY</h1>
  <div class="abs hero-dots"></div>
  <p class="abs hero-text">Sed ut perspiciatis unde omnis iste natus error sit voluptatem accusantium doloremque laudantium, totam rem aperiam, eaque ipsa quae ab illo inventore veritatis et quasi architecto beatae vitae dicta sunt explicabo. Nemo enim ipsam voluptatem quia voluptas.</p>
  <div class="abs btn-hero">VIEW OUR PRODUCTS</div>
</section>

<div class="card lab" style="left:189px">
  <div class="head">
    <div class="icon"><svg width="36" height="36" viewBox="0 0 36 36"><path d="M13 4h10M15 4v10L6 30a2 2 0 0 0 2 3h20a2 2 0 0 0 2-3l-9-16V4" fill="none" stroke="#f05a22" stroke-width="2.5"/><path d="M10 24h16l3 6H7z" fill="#f05a22"/></svg></div>
  </div>
  <div class="label">LABORATORY</div>
  <p class="body">Sed ut perspiciatis unde omnis iste natus error sit voluptatem accusantium doloremque laudantium, totam rem aperiam, eaque ipsa quae ab illo inventore veritatis et quasi architecto beatae vitae dicta sunt explicabo. Nemo enim ipsam voluptatem quia voluptas.</p>
  <div class="plus">+</div>
</div>

<div class="card" style="left:470px">
  <div class="head">
    <div class="icon"><svg width="36" height="36" viewBox="0 0 36 36"><rect x="14" y="4" width="8" height="16" rx="2" fill="#f05a22" transform="rotate(-25 18 12)"/><path d="M8 32h22M12 32a10 10 0 0 1 14-14" fill="none" stroke="#f05a22" stroke-width="3"/></svg></div>
    <div class="title" style="top:176px">RESEARCHES</div>
  </div>
  <p class="body">Sed ut perspiciatis unde omnis iste natus error sit voluptatem accusantium doloremque laudantium, totam rem aperiam, eaque ipsa quae ab illo inventore veritatis et quasi architecto beatae vitae dicta sunt explicabo. Nemo enim ipsam voluptatem quia voluptas.</p>
  <div class="plus">+</div>
</div>

<div class="card" style="left:751px">
  <div class="head">
    <div class="icon"><svg width="36" height="36" viewBox="0 0 36 36"><g stroke="#f05a22" stroke-width="2.5"><line x1="10" y1="26" x2="18" y2="16"/><line x1="18" y1="16" x2="28" y2="10"/><line x1="18" y1="16" x2="26" y2="28"/></g><g fill="#f05a22"><circle cx="10" cy="26" r="4"/><circle cx="18" cy="16" r="4"/><circle cx="28" cy="10" r="4"/><circle cx="26" cy="28" r="4"/></g></svg></div>
    <div class="title" style="top:176px">TECHNOLOGIES</div>
  </div>
  <p class="body">Sed ut perspiciatis unde omnis iste natus error sit voluptatem accusantium doloremque laudantium, totam rem aperiam, eaque ipsa quae ab illo inventore veritatis et quasi architecto beatae vitae dicta sunt explicabo. Nemo enim ipsam voluptatem quia voluptas.</p>
  <div class="plus">+</div>
</div>

<div class="abs shadow"></div>

<h2 class="abs section-title">OUR PRODUCTS</h2>
<div class="arrow-round" style="left:28px;top:1497px">&#8249;</div>
<div class="product" style="left:82px"><div class="photo" role="img" aria-label="Medicine vial with blue cap" style="background:linear-gradient(180deg,#d2d2d2,#bdbdbd)"></div><div class="bar">DOLOREMQUE LAUDAN<span>&#8250;</span></div></div>
<div class="product" style="left:342px"><div class="photo" role="img" aria-label="Medicine vial with teal cap"></div><div class="bar">DOLOREMQUE LAUDAN<span>&#8250;</span></div></div>
<div class="product" style="left:602px"><div class="photo" role="img" aria-label="Medicine vial with green cap"></div><div class="bar">DOLOREMQUE LAUDAN<span>&#8250;</span></div></div>
<div class="product" style="left:864px"><div class="photo" role="img" aria-label="Medicine vial with purple cap"></div><div class="bar">DOLOREMQUE LAUDAN<span>&#8250;</span></div></div>
<div class="arrow-round" style="left:1133px;top:1497px">&#8250;</div>

<section class="abs about">
  <div class="abs welcome-kicker">WELCOME TO</div>
  <div class="abs welcome-name">PRAIRIE BIO</div>
  <p class="abs welcome-text">The purpose of the Lakeside Biopharmaceutical Statistics Workshop is to foster discussion on statistical methodology in the pharmaceutical industry. The next edition is May 19-21, 2014. The first annual conference was held in 1978. The founders decided to proceed with a conference emphasis on the applications and theory relevant to the pharmaceutical industry. Since the pharmaceutical industry spanned a wide range of research and development activity – basic biological and chemical research, clinical research, process development, assay development, dosage form development, stability, quality control, quality assurance, and manufacturing – it</p>
  <div class="btn-navy" style="left:417px;top:320px;width:148px">Read more<span>&#8250;</span></div>

  <div class="abs divider"></div>

  <div class="abs blog-title">BLOG</div>
  <div class="arrow-round" style="left:680px;top:111px">&#8249;</div>
  <div class="abs blog-photo" role="img" aria-label="Scientist examining a test tube in a lab"></div>
  <div class="arrow-round" style="left:1075px;top:111px">&#8250;</div>
  <div class="abs blog-post-title">OQUE PENATIBUS ET MAGNIS DIS PARTURIENT</div>
  <p class="abs blog-text">The purpose of the Lakeside Biopharmaceutical Statistics Workshop is to foster discussion on statistical methodology in the pharmaceutical</p>
  <div class="abs blog-meta">
    <div><svg width="24" height="24" viewBox="0 0 24 24"><circle cx="12" cy="13" r="8" fill="none" stroke="#f05a22" stroke-width="2"/><path d="M12 9v4l3 2" fill="none" stroke="#f05a22" stroke-width="2"/></svg>12/2014</div>
    <div><svg width="24" height="22" viewBox="0 0 24 22"><path d="M3 3h18v12H9l-5 4v-4H3z" fill="none" stroke="#f05a22" stroke-width="2"/></svg>04</div>
  </div>
  <div class="btn-navy" style="left:987px;top:320px;width:145px">See All<span>&#8250;</span></div>
</section>

<section class="abs testimonial" role="img" aria-label="Blurred laboratory flasks with coloured liquids">
  <div class="shade"></div>
  <div class="t-arrow" style="left:104px">&#8249;</div>
  <div class="abs quote-circle">&#8220;</div>
  <div class="abs avatar-circle"><svg width="60" height="60" viewBox="0 0 60 60"><circle cx="30" cy="20" r="12" fill="#fff"/><path d="M8 54a22 18 0 0 1 44 0z" fill="#fff"/></svg></div>
  <div class="abs t-line"></div>
  <div class="abs t-title">OQUE PENATIBUS ET MAGNIS DIS PARTURIENT</div>
  <p class="abs t-text">The purpose of the Lakeside Biopharmaceutical Statistics Workshop is to foster discussion on statistical methodology in the pharmaceutical industry. The next edition is May 19-21, 2014. The first annual conference was held in 1978. The founders decided to proceed with a conference</p>
  <div class="abs t-name">DR. ALAN PIERCE</div>
  <div class="abs t-role">Biopharmacist</div>
  <div class="t-arrow" style="left:1068px">&#8250;</div>
</section>

<section class="abs news">
  <svg class="abs" style="left:583px;top:24px" width="34" height="24" viewBox="0 0 34 24"><rect width="34" height="24" fill="#222"/><path d="M0 0l17 13L34 0" fill="none" stroke="#f3f3f3" stroke-width="2"/></svg>
  <div class="abs news-title">SUBSCRIBE TO OUR NEWS LETTER</div>
  <div class="abs news-input">Enter your email address</div>
  <div class="abs news-submit">SUBMIT</div>
</section>

<footer class="abs footer">
  <div class="social" style="left:503px"></div>
  <div class="social" style="left:575px"></div>
  <div class="social" style="left:650px"></div>
  <div class="social" style="left:721px"></div>
  <div class="abs f-address">
    <svg width="28" height="24" viewBox="0 0 28 24"><path d="M14 1L1 12h4v11h7v-7h4v7h7V12h4z" fill="#fff"/></svg>
    Harbor Hall Lindenfield, Ohio, United States
  </div>
  <div class="abs f-phone">
    <svg width="26" height="26" viewBox="0 0 24 24"><path fill="#fff" d="M6.6 10.8a15 15 0 0 0 6.6 6.6l2.2-2.2a1 1 0 0 1 1-.25 11.4 11.4 0 0 0 3.6.57 1 1 0 0 1 1 1V20a1 1 0 0 1-1 1A17 17 0 0 1 3 4a1 1 0 0 1 1-1h3.5a1 1 0 0 1 1 1c0 1.25.2 2.45.57 3.57a1 1 0 0 1-.25 1z"/></svg>
    1-800-555-0142
  </div>
  <div class="abs f-copy">© 2014 prairie bio | privacy policy</div>
</footer>

</body>
</html>
```